Book cover for "Eczema turnaround"

Hi, we need a book cover for "Eczema turnaround" book.
It's a book about how to cure psoriasis symptoms which appeared to be results of stress.
The main theme in this book is that all symptoms are psychosomatic and can be cut short by reducing the level of stress.
Cover has to be bold and speaking. It has to show the results,
PLEASE consider using photos or illustrations "before" and "after".
Or maybe you can propose your vision.

3D image and 2D image.
Please see the links, it will be helpful for you to create image form.
http://kx7wqrna.lumvexo.com/?skip-tracking=true
http://tz3mbfuc.lumvexo.com/?skip-tracking=true

Target Market(s)

TA is very wide, it's all people who experienced decease demonstration. Usually these people very embarrassed of their illness, they are under high level of stress and what they need it's hope and believe that they can relief their condition.

Requirements
Must have
• Author name:
Pavel Drenko
Titlle :
Eczema turnaround
Subtitle:
ECZEMA TURNAROUND:
REDUCE THE RASH AND ITCHING 73% WITH THIS SIMPLE TECHNIQUE

```html
<!DOCTYPE html>
<html lang="en">
<head>
<meta charset="utf-8">
<title>Eczema Turnaround — Pavel Drenko</title>
<link href="https://fonts.googleapis.com/css2?family=Cinzel:wght@400;700&family=Cormorant+SC:wght@500;600&display=swap" rel="stylesheet">
<style>
  :root {
    --cover-black: #050505;
    --skin-light: #d9a98c;
    --skin-mid: #b98064;
    --rash-red: #b8455a;
    --title-white: #ffffff;
    --band-white: #ffffff;
    --accent-pink: #e8288a;
    --text-white: #f4f4f4;
  }
  * { margin: 0; padding: 0; box-sizing: border-box; }
  html, body {
    width: 890px;
    height: 1200px;
    overflow: hidden;
    background: var(--cover-black);
  }
  .book-cover {
    position: relative;
    width: 890px;
    height: 1200px;
    overflow: hidden;
    background: var(--cover-black);
  }
  .cover-photo {
    position: absolute;
    inset: 0;
    background:
      radial-gradient(ellipse 30% 55% at 62% 38%, rgba(184,69,90,0.35), transparent 70%),
      linear-gradient(90deg,
        var(--cover-black) 0%,
        var(--cover-black) 14%,
        var(--skin-mid) 24%,
        var(--skin-light) 36%,
        var(--skin-mid) 49%,
        var(--skin-light) 62%,
        var(--skin-mid) 76%,
        var(--cover-black) 88%,
        var(--cover-black) 100%);
  }
  .author-name {
    position: absolute;
    top: 66px;
    left: 0;
    width: 100%;
    text-align: center;
    font-family: "Cormorant SC", serif;
    font-weight: 500;
    font-size: 30px;
    letter-spacing: 1px;
    color: var(--text-white);
  }
  .title-main {
    position: absolute;
    top: 530px;
    left: 0;
    width: 100%;
    text-align: center;
    font-family: "Cinzel", serif;
    font-weight: 400;
    font-size: 156px;
    line-height: 1;
    letter-spacing: 2px;
    color: var(--title-white);
  }
  .title-band {
    position: absolute;
    top: 672px;
    left: 46px;
    right: 46px;
    height: 100px;
    background: var(--band-white);
    display: flex;
    align-items: center;
    justify-content: center;
  }
  .title-accent {
    font-family: "Cinzel", serif;
    font-weight: 400;
    font-size: 86px;
    letter-spacing: 1px;
    color: var(--accent-pink);
    line-height: 1;
  }
  .subtitle {
    position: absolute;
    top: 792px;
    left: 0;
    width: 100%;
    text-align: center;
    font-family: "Cormorant SC", serif;
    font-weight: 600;
    font-size: 31px;
    line-height: 1.15;
    letter-spacing: 1px;
    color: var(--text-white);
  }
</style>
</head>
<body>
  <main class="book-cover">
    <div class="cover-photo" role="img" aria-label="Photograph of a person's bare legs standing on a black background, one leg clear and the other covered with red eczema patches, showing before and after"></div>
    <p class="author-name">PAVEL DRENKO</p>
    <h1 class="title-main">ECZEMA</h1>
    <div class="title-band">
      <span class="title-accent">TURNAROUND</span>
    </div>
    <p class="subtitle">REDUCE THE RASH AND ITCHING 73%<br>WITH THIS SIMPLE TECHNIQUE</p>
  </main>
</body>
</html>
```